Create Brisk Lesson Studio a card design that will stick in the mind of prospects.

Brisk Lesson Studio specialises designs and produces training video, animation, illustration and text.

We need a card design that oozes class and leaves the prospect brimming with confidence.

The design will feature the Brisk Lesson Studio all black logo (uploaded). The design may also use the shade of orange from the orange version of the logo (uploaded). Note, just the color is to be used e.g. for the back of the card, not the orange logo itself.

The Brisk brand is about authenticity, quality, maturity and assurance. We are a safe buy when it comes to the prospects next project.

Target Market(s)

The primary target is training managers or others who are responsible for choosing to hire companies to produce their training media e.g. video. This will usually be a large spend so they need to have confidence.

Industry/Entity Type

Training

Contact Information for Business Card

FRONT:

Brisk Lesson Studio
Phone: 03 5172 4039
1st Floor, 418 Kellerby Road
Mt Ferncombe
VIC 3862
Australia
www.brisklesson.com.au

Lionel Petch
Founder and Lead Consultant
mobile: +61 3 0462 735 218
email: lionel@brisklesson.com.au

BACK:
Specialising in design and production of training:

video
animation
illustration
text

for delivery via internet, intranet and/or LMS.

Number of Pages Required

4 page

Font styles to use
Sans Serif

Requirements
Must have
• The black logo uploaded with the brief.
Nice to have
• The inclusion of the shade of orange found in the orange logo also uploaded with the brief. One example would be having the back of the card in this orange and using a white font for the text. But I want the designer to work this out.
Should not have
• No colours other than black and the orange included in the uploaded orange logo.

```html
<!DOCTYPE html>
<html lang="en">
<head>
<meta charset="utf-8">
<title>Brisk Lesson Studio – Business Card</title>
<link rel="stylesheet" href="https://fonts.googleapis.com/css2?family=Titillium+Web:wght@400;600;700&display=swap">
<style>
  :root {
    --bg: #e4e4e4;
    --card: #ffffff;
    --orange: #f26322;
    --black: #1a1a1a;
    --ink: #333333;
    --ghost: #f0f0f0;
  }
  * { margin: 0; padding: 0; box-sizing: border-box; }
  html, body { width: 1200px; height: 800px; overflow: hidden; }
  body {
    background: var(--bg);
    font-family: "Titillium Web", Arial, sans-serif;
    color: var(--ink);
    position: relative;
  }
  .card {
    position: absolute;
    top: 281px;
    width: 430px;
    height: 238px;
    background: var(--card);
    overflow: hidden;
  }
  .card-front { left: 110px; }
  .card-back { left: 660px; }

  .front-shapes { position: absolute; inset: 0; }

  .ghost-name {
    position: absolute;
    left: 14px;
    top: 174px;
    font-weight: 700;
    font-size: 62px;
    line-height: 1;
    color: var(--ghost);
  }

  .holder {
    position: absolute;
    left: 163px;
    top: 46px;
  }
  .holder-name {
    font-size: 20px;
    font-weight: 600;
    line-height: 1.1;
    color: var(--black);
  }
  .holder-name .first { color: var(--orange); }
  .holder-role {
    font-size: 13px;
    line-height: 1.2;
    color: var(--black);
  }

  .contact-col {
    position: absolute;
    top: 116px;
    font-size: 9.5px;
    line-height: 14px;
    color: var(--ink);
    white-space: nowrap;
  }
  .contact-col .icon {
    display: block;
    width: 18px;
    height: 18px;
    margin-bottom: 10px;
  }
  .col-phone { left: 24px; }
  .col-phone .icon { margin-left: 36px; }
  .col-web { left: 138px; }
  .col-web .icon { margin-left: 48px; }
  .col-address { left: 262px; }
  .col-address .icon { margin-left: 58px; }

  .back-content {
    position: absolute;
    inset: 0;
    display: flex;
    flex-direction: column;
    align-items: center;
    justify-content: center;
    gap: 14px;
  }
  .brand-mark {
    display: flex;
    align-items: center;
    gap: 12px;
  }
  .brand-dot {
    width: 22px;
    height: 22px;
    border-radius: 50%;
    background: var(--black);
  }
  .brand-name {
    font-weight: 700;
    font-size: 30px;
    color: var(--black);
    line-height: 1;
  }
  .services {
    text-align: center;
    font-size: 10px;
    line-height: 14px;
    color: var(--ink);
  }
  .services .list {
    color: var(--orange);
    font-weight: 600;
  }
</style>
</head>
<body>

<section class="card card-front" aria-label="Card front">
  <svg class="front-shapes" width="430" height="238" viewBox="0 0 430 238">
    <path d="M0 0 H170 C105 6 40 30 0 76 Z" fill="var(--orange)"/>
    <path d="M0 76 C40 30 105 6 170 0 H182 C115 8 45 34 0 84 Z" fill="var(--black)"/>
    <path d="M430 150 C400 205 330 232 262 238 H430 Z" fill="var(--orange)"/>
    <path d="M430 146 C400 202 330 230 250 238 H262 C330 232 400 205 430 150 Z" fill="var(--black)"/>
  </svg>

  <div class="ghost-name">Brisk</div>

  <div class="holder">
    <p class="holder-name"><span class="first">Lionel</span> Petch</p>
    <p class="holder-role">Founder and Lead Consultant</p>
  </div>

  <div class="contact-col col-phone">
    <svg class="icon" viewBox="0 0 18 18" aria-hidden="true">
      <rect x="4" y="4" width="10" height="10" transform="rotate(45 9 9)" fill="none" stroke="var(--orange)" stroke-width="1"/>
      <path d="M7 6.5 l1 -0.5 l1 1.6 l-0.7 0.6 q0.5 1.2 1.5 1.7 l0.6 -0.7 l1.6 1 l-0.5 1 q-3.5 -0.5 -4.5 -4.7 z" fill="var(--orange)"/>
    </svg>
    <p>P 03 5172 4039</p>
    <p>M +61 3 0462 735 218</p>
  </div>

  <div class="contact-col col-web">
    <svg class="icon" viewBox="0 0 18 18" aria-hidden="true">
      <rect x="4" y="4" width="10" height="10" transform="rotate(45 9 9)" fill="none" stroke="var(--orange)" stroke-width="1"/>
      <circle cx="9" cy="9" r="2.8" fill="none" stroke="var(--orange)" stroke-width="0.9"/>
      <path d="M6.2 9 H11.8 M9 6.2 V11.8" stroke="var(--orange)" stroke-width="0.7"/>
    </svg>
    <p>lionel@brisklesson.com.au</p>
    <p>www.brisklesson.com.au</p>
  </div>

  <div class="contact-col col-address">
    <svg class="icon" viewBox="0 0 18 18" aria-hidden="true">
      <rect x="4" y="4" width="10" height="10" transform="rotate(45 9 9)" fill="none" stroke="var(--orange)" stroke-width="1"/>
      <path d="M9 12 C7.5 10 7 9 7 8 a2 2 0 0 1 4 0 c0 1 -0.5 2 -2 4 z" fill="var(--orange)"/>
      <circle cx="9" cy="8" r="0.7" fill="var(--card)"/>
    </svg>
    <p>1st Floor, 418 Kellerby Road</p>
    <p>Mt Ferncombe VIC 3862, Australia</p>
  </div>
</section>

<section class="card card-back" aria-label="Card back">
  <div class="back-content">
    <div class="brand-mark">
      <span class="brand-dot" aria-hidden="true"></span>
      <span class="brand-name">Brisk Lesson Studio</span>
    </div>
    <div class="services">
      <p>Specialising in design and production of training</p>
      <p class="list">video · animation · illustration · text</p>
      <p>for delivery via internet, intranet and/or LMS</p>
    </div>
  </div>
</section>

</body>
</html>
```